landscaping core flute signs

I need core flutes created with business name and a few extra dot points for putting on fences for job sites 120cm x 120cm approx.
I want our old ones information with the new L logo and colour palette

```html
<!DOCTYPE html>
<html lang="en">
<head>
<meta charset="utf-8">
<title>Grounded Form – Job Site Sign</title>
<link rel="stylesheet" href="https://fonts.googleapis.com/css2?family=Poppins:wght@500;600&display=swap">
<style>
  :root {
    --ink: #111111;
    --leaf: #5f935a;
    --paper: #ffffff;
  }
  html, body {
    margin: 0;
    padding: 0;
    width: 1200px;
    height: 1200px;
    overflow: hidden;
    background: var(--paper);
    font-family: "Poppins", Arial, sans-serif;
  }
  .sign {
    position: relative;
    width: 1200px;
    height: 1200px;
  }
  .frame-lines {
    position: absolute;
    inset: 0;
  }
  .brand {
    position: absolute;
    left: 0;
    right: 0;
    top: 262px;
    text-align: center;
  }
  .brand-dot {
    width: 148px;
    height: 148px;
    border-radius: 50%;
    background: var(--leaf);
    margin: 0 auto 22px;
  }
  .brand-name {
    margin: 0;
    font-weight: 600;
    font-size: 50px;
    letter-spacing: 2px;
    color: var(--ink);
    line-height: 1;
  }
  .services {
    position: absolute;
    left: 334px;
    top: 540px;
    margin: 0;
    padding: 0;
    list-style: none;
  }
  .service {
    display: flex;
    align-items: center;
    height: 64px;
    font-weight: 600;
    font-size: 41px;
    color: var(--ink);
    letter-spacing: 0.3px;
    white-space: nowrap;
  }
  .service::before {
    content: "";
    width: 40px;
    height: 40px;
    border-radius: 50%;
    background: var(--leaf);
    margin-right: 12px;
    flex: none;
  }
  .contact-bar {
    position: absolute;
    left: 238px;
    top: 752px;
    width: 698px;
    height: 44px;
  }
  .contact-phone, .contact-email {
    position: absolute;
    top: 0;
    height: 44px;
    display: flex;
    align-items: center;
    color: var(--paper);
    font-weight: 500;
    white-space: nowrap;
    box-sizing: border-box;
  }
  .contact-phone {
    left: 0;
    width: 360px;
    background: var(--ink);
    clip-path: polygon(0 0, 100% 0, 95% 100%, 0 100%);
    font-size: 30px;
    letter-spacing: 1px;
    padding-left: 34px;
  }
  .contact-email {
    left: 338px;
    width: 360px;
    background: var(--leaf);
    clip-path: polygon(5% 0, 100% 0, 100% 100%, 0 100%);
    font-size: 20px;
    padding-left: 24px;
  }
  .contact-phone svg { margin-right: 14px; flex: none; }
  .contact-email svg { margin-right: 8px; flex: none; }
  .ground-art {
    position: absolute;
    left: 240px;
    top: 800px;
    width: 722px;
    height: 164px;
    background: linear-gradient(100deg, var(--ink) 0%, #2c3a2b 50%, var(--leaf) 80%);
  }
</style>
</head>
<body>
<main class="sign">
  <svg class="frame-lines" width="1200" height="1200" viewBox="0 0 1200 1200" aria-hidden="true">
    <rect x="232" y="232" width="736" height="736" fill="none" stroke="#111" stroke-width="8"/>
    <g stroke="#111" stroke-width="4" fill="none">
      <line x1="236" y1="242" x2="964" y2="242"/>
      <line x1="236" y1="258" x2="964" y2="258"/>
      <line x1="242" y1="236" x2="242" y2="800"/>
      <line x1="258" y1="236" x2="258" y2="800"/>
      <line x1="942" y1="236" x2="942" y2="800"/>
      <line x1="958" y1="236" x2="958" y2="800"/>
    </g>
  </svg>

  <header class="brand">
    <div class="brand-dot"></div>
    <h1 class="brand-name">GROUNDED FORM</h1>
  </header>

  <ul class="services">
    <li class="service">PAVING &amp; CONCRETING</li>
    <li class="service">FENCING &amp; RETAINING</li>
    <li class="service">DESIGN &amp; CONSTRUCT</li>
  </ul>

  <div class="contact-bar">
    <div class="contact-phone">
      <svg width="26" height="26" viewBox="0 0 24 24" aria-hidden="true">
        <circle cx="12" cy="12" r="12" fill="#fff"/>
        <path d="M8.2 6.5l1.8-.4 1.2 2.8-1.3 1c.6 1.4 1.6 2.4 3 3l1-1.3 2.8 1.2-.4 1.8c-4.6.4-8.5-3.5-8.1-8.1z" fill="#111"/>
      </svg>
      0412 555 903
    </div>
    <div class="contact-email">
      <svg width="20" height="20" viewBox="0 0 24 24" aria-hidden="true" fill="none" stroke="#fff" stroke-width="1.8">
        <circle cx="12" cy="12" r="10"/>
        <ellipse cx="12" cy="12" rx="4.5" ry="10"/>
        <line x1="2" y1="12" x2="22" y2="12"/>
      </svg>
      sam@groundedform.com
    </div>
  </div>

  <div class="ground-art" role="img" aria-label="Decorative band of black and green stepping-stone pebbles beneath a row of green fern leaves"></div>
</main>
</body>
</html>
```